Documentary Film Poster Design

I need a vertical movie poster for my documentary film,
Some images are attached to incorporate. You can use one or a few....Here is the trailer for the film so you can get an idea of the movie.
https://streamloft.net/584213097
Here is a brief synopsis:
In the lush rainforest of Bocas del Toro, Panama, an indigenous cacao farmer, his wife and grandchildren confront environmental and economic complexities as they grow, harvest and sell cacao beans for a global chocolate market. Does Fair Trade Certification really work? Documenting the exceptional wisdom, unconditional devotion and proven ancient farming techniques of one hard-working Ngäbe farmer, Tomás Quintero, Sin Orilla complicates the question by examining the fairness of his trade.
Here is the text I want on the poster:
Quiet Heron Productions presents
Sin Orilla
A Film by Renata J. Osorio
A Fair Trade certified farmer questions the true fairness of his trade.
www.sinorillafilm.com
Please be creative and let me know if you have questions.
Movie

```html
<!DOCTYPE html>
<html lang="en">
<head>
<meta charset="utf-8">
<title>Sin Orilla — Poster</title>
<link rel="stylesheet" href="https://fonts.googleapis.com/css2?family=Cormorant+Garamond:ital,wght@0,500;1,500&family=Montserrat:wght@400;600&family=Raleway:wght@400&display=swap">
<style>
  :root {
    --bean-dark: #1f1c12;
    --bean-deep: #3c3a26;
    --bean-olive: #66644a;
    --bean-sage: #8e8c6e;
    --bean-light: #a9a88c;
    --skin-warm: #c99a74;
    --skin-mid: #a87552;
    --skin-shadow: #5a3a24;
    --ink-white: #ffffff;
  }
  * { margin: 0; padding: 0; box-sizing: border-box; }
  html, body { width: 800px; height: 1200px; overflow: hidden; background: var(--bean-dark); }
  .poster {
    position: relative;
    width: 800px;
    height: 1200px;
    overflow: hidden;
    color: var(--ink-white);
    text-align: center;
  }
  .poster-photo {
    position: absolute;
    inset: 0;
    background:
      radial-gradient(ellipse 32% 10% at 28% 12%, var(--skin-warm) 0%, transparent 100%),
      radial-gradient(ellipse 22% 8% at 12% 28%, var(--skin-mid) 0%, transparent 100%),
      radial-gradient(ellipse 20% 7% at 22% 38%, var(--skin-warm) 0%, transparent 100%),
      radial-gradient(ellipse 24% 8% at 70% 41%, var(--skin-mid) 0%, transparent 100%),
      radial-gradient(ellipse 28% 12% at 82% 22%, var(--bean-light) 0%, transparent 100%),
      radial-gradient(ellipse 30% 14% at 60% 58%, var(--bean-sage) 0%, transparent 100%),
      radial-gradient(ellipse 26% 12% at 20% 60%, var(--bean-sage) 0%, transparent 100%),
      radial-gradient(ellipse 30% 12% at 80% 72%, var(--bean-olive) 0%, transparent 100%),
      radial-gradient(ellipse 45% 9% at 35% 90%, var(--skin-mid) 0%, transparent 100%),
      radial-gradient(ellipse 60% 12% at 50% 99%, var(--skin-shadow) 0%, transparent 100%),
      linear-gradient(170deg, var(--bean-deep) 0%, var(--bean-olive) 30%, var(--bean-deep) 55%, var(--bean-olive) 72%, var(--bean-dark) 100%);
  }
  .poster-veil {
    position: absolute;
    inset: 0;
    background:
      radial-gradient(ellipse 80% 70% at 50% 50%, transparent 40%, rgba(15,12,6,0.45) 100%),
      linear-gradient(180deg, rgba(20,16,10,0.1) 0%, rgba(20,16,10,0.25) 45%, rgba(20,16,10,0.1) 100%);
  }
  .poster-content { position: relative; height: 100%; }
  .studio-mark {
    position: absolute;
    top: 124px;
    left: 0; right: 0;
    display: flex;
    flex-direction: column;
    align-items: center;
  }
  .studio-dot {
    width: 54px; height: 54px;
    border-radius: 50%;
    background: var(--ink-white);
  }
  .studio-name {
    margin-top: 62px;
    font-family: "Cormorant Garamond", serif;
    font-weight: 500;
    font-variant: small-caps;
    font-size: 30px;
    line-height: 1;
    letter-spacing: 1px;
  }
  .studio-presents {
    font-family: "Cormorant Garamond", serif;
    font-style: italic;
    font-weight: 500;
    font-size: 28px;
    line-height: 1;
    margin-top: 12px;
  }
  .film-title {
    position: absolute;
    top: 478px;
    left: 0; right: 0;
    font-family: "Montserrat", sans-serif;
    font-weight: 600;
    font-size: 84px;
    letter-spacing: 8px;
    line-height: 1;
  }
  .film-credit {
    position: absolute;
    top: 598px;
    left: 0; right: 0;
    font-family: "Montserrat", sans-serif;
    font-weight: 400;
    font-size: 19px;
    letter-spacing: 2px;
  }
  .film-tagline {
    position: absolute;
    top: 698px;
    left: 0; right: 0;
    font-family: "Raleway", sans-serif;
    font-weight: 400;
    font-size: 31px;
    line-height: 54px;
    letter-spacing: 2px;
    text-transform: uppercase;
  }
  .film-site {
    position: absolute;
    top: 1148px;
    left: 0; right: 0;
    font-family: "Montserrat", sans-serif;
    font-weight: 600;
    font-size: 18px;
    letter-spacing: 9px;
    text-transform: uppercase;
  }
</style>
</head>
<body>
  <main class="poster">
    <div class="poster-photo" role="img" aria-label="Close-up photograph of a farmer's open hands holding a heap of dried cacao beans"></div>
    <div class="poster-veil"></div>
    <div class="poster-content">
      <header class="studio-mark">
        <span class="studio-dot"></span>
        <p class="studio-name">Quiet Heron Productions</p>
        <p class="studio-presents">Presents</p>
      </header>
      <h1 class="film-title">SIN ORILLA</h1>
      <p class="film-credit">A FILM BY RENATA J. OSORIO</p>
      <p class="film-tagline">A fair trade certified farmer<br>questions the true fairness<br>of his trade</p>
      <p class="film-site">www.sinorillafilm.com</p>
    </div>
  </main>
</body>
</html>
```